Pet Care company needs label design for new product. Eco-friendly, amazing results helping anima...

We need a label designed for a new eco-friendly pet care product. The product is highly effective, non-medicated, 100% safe to use on all animals. The product is an aqueous solution that uses a low PH to create an environment unfavorable for the grow of bacteria and fungus. Target market is horses, dogs and cats. Most common uses will be for rain rot, hot spots, ear infections and wound care. **Bottle is green with a white sprayer. Here is the specifications for the label; Trim size: 8.375 x 4.25 (w x h), please keep all critical art at least 1/8 inch away from trim line.Bleeds: Include 1/8 inch bleeds, and keep all critical art at least 1/8 inch away from trim line.

Target Market(s)

Pet owners; horses, dogs and cats

Industry/Entity Type

Pet Care

Font styles to use
Serif

Colors

Designer to choose colors to be used in the design.

Requirements
Must have
• Images of horses, dogs, cats. Geared to the eco-friendly nature of the product. It is not "organic" but I want that kind of look.
Nice to have
• Product information uploaded.
Should not have
• I do not want the product to look cartoonish. It is a highly effective treatment for animals with skin infections. I want people to feel by looking at the product it works.

```html
<!DOCTYPE html>
<html lang="en">
<head>
<meta charset="UTF-8">
<title>Marlow's Mend – Eco-Friendly Pet Care Label</title>
<link href="https://fonts.googleapis.com/css2?family=Outfit:wght@400;500;700;800&display=swap" rel="stylesheet">
<style>
  :root {
    --canvas: #f4f5f2;
    --label-dark: #1b5441;
    --label-mid: #226a55;
    --label-light: #2a7a62;
    --lime: #c6dc5a;
    --lime-text: #b3ca4a;
    --brand-ink: #1c5440;
    --body-text: #f2f5f0;
    --list-text: #dde7df;
  }
  * { box-sizing: border-box; margin: 0; padding: 0; }
  html, body { width: 1200px; height: 1000px; overflow: hidden; background: var(--canvas); }
  body { position: relative; font-family: "Outfit", Arial, sans-serif; }

  .label {
    position: absolute;
    left: 340px; top: 114px;
    width: 520px; height: 771px;
    background: linear-gradient(90deg, var(--label-dark) 0%, var(--label-mid) 45%, var(--label-light) 80%, var(--label-mid) 100%);
    color: var(--body-text);
  }
  .brand-banner {
    position: absolute;
    left: 83px; top: 27px;
    width: 349px; height: 160px;
  }
  .brand-banner svg { position: absolute; inset: 0; }
  .brand-name {
    position: absolute;
    left: 0; right: 0; top: 50px;
    text-align: center;
    font-size: 38px;
    font-weight: 500;
    letter-spacing: 0.5px;
    color: var(--brand-ink);
    line-height: 1;
  }
  .headline {
    position: absolute;
    left: 0; right: 0; top: 258px;
    text-align: center;
    font-size: 37px;
    font-weight: 800;
    color: var(--lime-text);
    line-height: 1;
  }
  .description {
    position: absolute;
    left: 60px; right: 60px; top: 330px;
    text-align: center;
    font-size: 14.5px;
    line-height: 24px;
    font-weight: 400;
  }
  .animal-emblem {
    position: absolute;
    left: 315px; top: 457px;
    width: 106px; height: 106px;
  }
  .uses {
    position: absolute;
    left: 59px; top: 546px;
    list-style: none;
    font-size: 22px;
    font-weight: 700;
    line-height: 41px;
    color: var(--list-text);
  }
  .volume {
    position: absolute;
    left: 0; right: 0; top: 743px;
    text-align: center;
    font-size: 11px;
    font-weight: 700;
  }
</style>
</head>
<body>
  <div class="label">
    <div class="brand-banner">
      <svg width="349" height="160" viewBox="0 0 349 160" aria-hidden="true">
        <polygon points="0,0 349,0 349,131 174.5,160 0,131" fill="var(--lime)"/>
      </svg>
      <div class="brand-name">MARLOW'S MEND</div>
    </div>

    <h1 class="headline">Eco-Friendly Pet Care</h1>

    <p class="description">None medicated,safe,effective aid<br>providing a&nbsp; healing environment for<br>recovery from fungal and bacterial infections.</p>

    <svg class="animal-emblem" viewBox="0 0 106 106" role="img" aria-label="Circular line illustration of a cat, dog and horse together">
      <circle cx="53" cy="53" r="50" fill="none" stroke="var(--lime-text)" stroke-width="2"/>
      <circle cx="53" cy="53" r="44" fill="var(--lime-text)" opacity="0.18"/>
    </svg>

    <ul class="uses">
      <li>Rain Rot - Hot Spots</li>
      <li>Surface wounds</li>
      <li>Ringworm and More!</li>
    </ul>

    <div class="volume">16 fl oz - 473 ml</div>
  </div>
</body>
</html>
```